Shop front signage design for Bubble Tea Shop

Plum Harbor is Sydney based Green Tea Shop.We are looking for a modern and sleek signage for shop front end. We have Aluminium Composite Panel and Awning sign at the shop front. We will keep Aluminium composite panel simple with logo and text. We are after awning design which is above glass door and under the panel. Old Awning is PVC foam in two pieces 2310mm w x 1000mm h. We need someone to design awing. It should reflect Bubble tea and using bubble tea cups with pearls is essential. Stock images can be used. Avoid using icons or illustrative icons as we are after real images of bubble tea cup. This is to ensure that the brand is not taken as juice shop or cafe.
Panel Dimensions is 5250 mm w x 580 mm h.Awning/ Fascia sign is 4720 mm w x 1000 mm h.
Logo and signage concept is attached.

Target Market(s)

Corporate Male and Female, school, general public.

Colors
f36e22
333333
000000
eaeaea
cbcbcb

Requirements
Must have
• Bubble tea cups with fruit or milk tea.
Should not have
• Icons, illustration

```html
<!DOCTYPE html>
<html lang="en">
<head>
<meta charset="utf-8">
<title>Plum Harbor – Awning Sign</title>
<link rel="stylesheet" href="https://fonts.googleapis.com/css2?family=Poppins:wght@500&family=Roboto+Condensed:wght@700&family=Kaushan+Script&family=Roboto:wght@500&display=swap">
<style>
  :root {
    --brand-orange: #f36e22;
    --ink: #000000;
    --charcoal: #333333;
    --paper: #ffffff;
    --backdrop: #eaeaea;
    --mist: #cbcbcb;
  }
  * { box-sizing: border-box; margin: 0; padding: 0; }
  html, body { width: 1200px; height: 960px; overflow: hidden; }
  body { background: var(--backdrop); position: relative; }

  .awning {
    position: absolute;
    left: 40px; top: 362px;
    width: 1120px; height: 236px;
    background: var(--paper);
    box-shadow: 0 3px 8px rgba(0,0,0,0.25);
    overflow: hidden;
  }
  .awning__band { position: absolute; inset: 0; width: 100%; height: 100%; }

  .brand {
    position: absolute;
    left: 49px; top: 86px;
    display: flex; align-items: center; gap: 14px;
    color: var(--paper);
  }
  .brand__dot {
    width: 80px; height: 80px;
    border: 5px solid var(--paper);
    border-radius: 50%;
  }
  .brand__name {
    font-family: "Poppins", sans-serif;
    font-weight: 500;
    font-size: 42px;
    letter-spacing: -0.5px;
    line-height: 1;
  }

  .drinks-photo {
    position: absolute;
    left: 539px; top: 20px;
    width: 344px; height: 156px;
    border-radius: 6px;
    background: linear-gradient(90deg, #e7e6f2 0%, #f6c6d6 25%, #f4ecaa 50%, #a8e0b8 72%, #f0c690 100%);
  }

  .tagline {
    position: absolute;
    right: 30px; top: 68px;
    text-align: right;
  }
  .tagline__fresh {
    display: block;
    font-family: "Kaushan Script", cursive;
    font-size: 54px;
    line-height: 1;
    color: var(--brand-orange);
  }
  .tagline__juice {
    display: block;
    font-family: "Roboto", sans-serif;
    font-weight: 500;
    font-size: 31px;
    line-height: 1.1;
    color: var(--ink);
  }

  .menu-list {
    position: absolute;
    left: 553px; right: 28px; top: 196px;
    display: flex; justify-content: space-between;
    list-style: none;
    font-family: "Roboto Condensed", sans-serif;
    font-weight: 700;
    font-size: 20px;
    color: var(--ink);
  }
  .menu-list__item { display: flex; align-items: center; gap: 5px; white-space: nowrap; }
  .menu-list__item::before {
    content: "";
    width: 13px; height: 13px;
    border-radius: 50%;
    background: var(--brand-orange);
  }
</style>
</head>
<body>
  <section class="awning">
    <svg class="awning__band" viewBox="0 0 1120 236" preserveAspectRatio="none" aria-hidden="true">
      <path d="M0 0 H465 Q475 150 535 236 H0 Z" fill="var(--brand-orange)"/>
      <path d="M478 0 Q486 140 548 236" fill="none" stroke="var(--brand-orange)" stroke-width="3"/>
    </svg>

    <div class="brand">
      <span class="brand__dot"></span>
      <span class="brand__name">Plum Harbor</span>
    </div>

    <div class="drinks-photo" role="img" aria-label="Photo of five bubble tea cups with straws and tapioca pearls: taro, strawberry, mango, green tea and milk tea"></div>

    <div class="tagline">
      <span class="tagline__fresh">Fresh</span>
      <span class="tagline__juice">Juice</span>
    </div>

    <ul class="menu-list">
      <li class="menu-list__item">Serving Pearl Tea</li>
      <li class="menu-list__item">Fruit Tea</li>
      <li class="menu-list__item">Green Tea</li>
      <li class="menu-list__item">Ice Frappe</li>
    </ul>
  </section>
</body>
</html>
```